디자인 카테고리
라벨(파우치) (식당/카페 업종)
브랜드 소개
20여가지의 싱글오리진 커피를 직접 로스팅해 마을의 주민들, 커피애호가들에게 원두와 음료로 판매해 온 새솔터원두상회. 가장 로컬의 정신에 충실하며 고객과의 커뮤니케이션으로 성장해 온 카페로 꼽히는 새솔터원두상회은 블랜딩(여러가지의 싱글 커피를 배합해 새로운 맛을 창출하는 것) 커피가 없는 집이기도 합니다.
새솔터원두상회이 2017년 상설화된 최초의 블랜딩 판매에 들어갑니다. 경복궁의 봄을 시작으로 한 네개의 연작이 출시 될 예정입니다. 경복궁의 처마와 잡상, 한글을 모티브로 한 현재의 로고에서 보이듯 새솔터원두상회이 소중하게 여기는 서촌과 도심의 문화자산에 대한 애정과 커피가 가진 한잔의 여유를 담아 주시기를 부탁드립니다.

```html
<!DOCTYPE html>
<html lang="ko">
<head>
<meta charset="utf-8">
<title>새솔터원두상회 — 달빛정원의 밤</title>
<link href="https://fonts.googleapis.com/css2?family=Nanum+Myeongjo:wght@400;700&family=Oswald:wght@300;400&display=swap" rel="stylesheet">
<style>
  :root {
    --page-bg: #f1eeee;
    --panel: #ffffff;
    --ink: #3a3a3a;
    --ink-soft: #555555;
    --badge: #6b6b6b;
    --swatch: #e4aeb8;
    --pink: #f6cfd6;
    --rose: #d9546f;
    --green: #6fb07a;
    --mint: #bfe3cf;
    --sky: #8ec7e6;
    --yellow: #f6cc63;
    --cream: #f7ecd8;
  }
  * { margin: 0; padding: 0; box-sizing: border-box; }
  html, body { width: 1200px; height: 1200px; overflow: hidden; }
  body { background: var(--page-bg); position: relative; font-family: "Nanum Myeongjo", serif; color: var(--ink); }

  .pouch-label {
    position: absolute; left: 260px; top: 146px; width: 680px; height: 904px; overflow: hidden;
  }
  .label-artwork {
    position: absolute; inset: 0;
    background:
      radial-gradient(circle at 75% 12%, var(--sky) 0 8%, transparent 22%),
      radial-gradient(circle at 60% 58%, #3c4a6b 0 6%, transparent 14%),
      radial-gradient(circle at 85% 40%, var(--pink) 0 12%, transparent 26%),
      radial-gradient(circle at 55% 80%, var(--yellow) 0 7%, transparent 18%),
      radial-gradient(circle at 90% 85%, var(--rose) 0 6%, transparent 20%),
      linear-gradient(180deg, var(--pink) 0%, var(--cream) 22%, var(--mint) 40%, var(--green) 52%, var(--cream) 64%, var(--rose) 74%, var(--pink) 86%, var(--green) 100%);
  }

  .info-panel {
    position: absolute; left: 30px; top: 30px; width: 264px; height: 844px;
    background: var(--panel); overflow: hidden;
  }
  .brand-mark {
    position: absolute; left: 84px; top: 56px; width: 108px; height: 108px; border-radius: 50%;
    background: var(--badge); color: #fff;
    display: flex; flex-direction: column; align-items: center; justify-content: center; text-align: center;
  }
  .brand-name { font-size: 17px; font-weight: 700; line-height: 1.25; width: 70px; }
  .brand-sub { font-size: 7px; margin-top: 4px; letter-spacing: .5px; }

  .blend-title {
    position: absolute; left: 30px; top: 192px; width: 220px;
    font-size: 42px; font-weight: 400; line-height: 1.2; letter-spacing: -1px;
    white-space: nowrap;
  }
  .blend-title .en {
    display: inline-block; vertical-align: middle; margin-left: 8px;
    font-size: 11px; line-height: 1.35; letter-spacing: .5px; font-weight: 400;
  }

  .story {
    position: absolute; left: 30px; top: 362px; width: 220px;
    font-size: 13px; line-height: 1.75; color: var(--ink-soft);
  }
  .story p + p { margin-top: 12px; }

  .flavor-notes {
    position: absolute; left: 30px; top: 614px; list-style: none;
    font-family: "Oswald", sans-serif; font-weight: 300; font-size: 14px; color: var(--ink-soft);
  }
  .flavor-notes li { display: flex; align-items: center; height: 29px; line-height: 1; }
  .flavor-notes li::before {
    content: ""; width: 14px; height: 14px; background: var(--swatch); margin-right: 12px; flex: none;
  }
</style>
</head>
<body>
  <main class="pouch-label">
    <div class="label-artwork" role="img" aria-label="화사한 꽃나무와 겹겹의 물결 언덕, 구름 사이에 자리한 전통 궁궐 누각을 그린 일러스트"></div>

    <section class="info-panel">
      <div class="brand-mark">
        <span class="brand-name">새솔터원두상회</span>
        <span class="brand-sub">cafe roasters</span>
      </div>

      <h1 class="blend-title">달빛정원의<br>밤<span class="en">NIGHT<br>OF THE MEADOW</span></h1>

      <div class="story">
        <p>당신이 따뜻해서 봄이 왔습니다.</p>
        <p>경회루 수양벚꽃 사이로<br>흩날리는 맑은 햇살과<br>꽃으로 시작되는<br>계절의 달콤함을 담았습니다.</p>
        <p>"달빛정원의 밤" 블렌딩은<br>가는 곳마다 따라다닐 것만 같은<br>꽃향기로 봄을 더 아름답게 합니다.</p>
      </div>

      <ul class="flavor-notes">
        <li>COFFEE BLOSSOM</li>
        <li>STRAWBERRY</li>
        <li>WILD BERRY</li>
        <li>COTTON CANDY</li>
        <li>CUSTARD</li>
        <li>HONEY</li>
        <li>GOOD BALANCED</li>
      </ul>
    </section>
  </main>
</body>
</html>
```